Business Card Design Project

double sided, embossed, name & logo on front font sonsie one, back Name Marisol Venkamp, mobile 0468201934, Phone 73519086,
email marisol@brightspanservices.com, use sysbols on the back for example an envelope for email, a telephone for phone number etc.symbol slate grey writing navy blue

Industry/Entity Type

Business

```html
<!DOCTYPE html>
<html lang="en">
<head>
<meta charset="utf-8">
<title>Brightspan Services – Business Card</title>
<link href="https://fonts.googleapis.com/css2?family=Sonsie+One&family=Open+Sans:wght@400;600&display=swap" rel="stylesheet">
<style>
  :root {
    --page-bg: #e9ebee;
    --card-white: #ffffff;
    --blue-light: #22b1e0;
    --blue-deep: #0c8dc0;
    --navy: #1b4f7d;
    --slate: #6b7a89;
    --white: #ffffff;
  }
  * { box-sizing: border-box; margin: 0; padding: 0; }
  html, body {
    width: 1200px;
    height: 900px;
    overflow: hidden;
    background: var(--page-bg);
  }
  .canvas {
    position: relative;
    width: 1200px;
    height: 900px;
  }
  .card {
    position: absolute;
    left: 290px;
    width: 620px;
    height: 378px;
    border-radius: 4px;
    box-shadow: 0 6px 18px rgba(30, 40, 55, 0.18);
    overflow: hidden;
  }
  /* Front side */
  .card-front {
    top: 50px;
    background: radial-gradient(ellipse at 45% 30%, var(--blue-light) 0%, var(--blue-deep) 100%);
  }
  .brand-name {
    position: absolute;
    font-family: "Open Sans", sans-serif;
    font-weight: 600;
    white-space: nowrap;
    letter-spacing: 0.5px;
  }
  .card-front .brand-name {
    left: 46px;
    bottom: 62px;
    font-size: 30px;
    color: var(--white);
  }
  /* Back side */
  .card-back {
    top: 470px;
    background: var(--card-white);
  }
  .holder-name {
    position: absolute;
    left: 150px;
    top: 44px;
    font-family: "Sonsie One", cursive;
    font-size: 22px;
    font-weight: 400;
    color: var(--navy);
  }
  .contact-list {
    position: absolute;
    left: 112px;
    top: 92px;
    list-style: none;
    font-family: "Open Sans", sans-serif;
    font-size: 15px;
    color: var(--navy);
  }
  .contact-list li {
    display: flex;
    align-items: center;
    gap: 12px;
    height: 27px;
  }
  .contact-icon {
    width: 16px;
    height: 16px;
    flex: none;
    fill: none;
    stroke: var(--slate);
    stroke-width: 1.6;
  }
  .card-back .brand-name {
    left: 44px;
    bottom: 70px;
    font-size: 38px;
    color: var(--navy);
  }
</style>
</head>
<body>
<main class="canvas">

  <section class="card card-front" aria-label="Card front">
    <span class="brand-name">Brightspan Services</span>
  </section>

  <section class="card card-back" aria-label="Card back">
    <h1 class="holder-name">Marisol Venkamp</h1>
    <ul class="contact-list">
      <li>
        <svg class="contact-icon" viewBox="0 0 16 16" aria-label="Mobile">
          <rect x="4" y="1" width="8" height="14" rx="1.5"/>
          <line x1="7" y1="12.5" x2="9" y2="12.5"/>
        </svg>
        <span>0468 201 934</span>
      </li>
      <li>
        <svg class="contact-icon" viewBox="0 0 16 16" aria-label="Phone">
          <path d="M4 1.5 L6.5 4.5 L5 6.5 C6 8.5 7.5 10 9.5 11 L11.5 9.5 L14.5 12 L12.5 14.5 C7 14 2 9 1.5 3.5 Z"/>
        </svg>
        <span>7351 9086</span>
      </li>
      <li>
        <svg class="contact-icon" viewBox="0 0 16 16" aria-label="Email">
          <rect x="1.5" y="3.5" width="13" height="9" rx="1"/>
          <polyline points="1.5,4 8,9 14.5,4"/>
        </svg>
        <span>marisol@brightspanservices.com</span>
      </li>
    </ul>
    <span class="brand-name">Brightspan Services</span>
  </section>

</main>
</body>
</html>
```